Lagoonworks Solutions

I run an aquarium service business covering all aspects of large scale saltwater aquariums. Design, installation, and service. My main customer base is corporations in Manhattan, but I also deal with smaller home or business aquariums in the tri-state area. I work with cutting edge equipment and service techniques and need to convey that.

Industry/Entity Type

Business

Contact Information for Business Card

LAGOONWORKS SOLUTIONS LLC
Jonathan R. Delvoy
Owner
Main 415-555-0182
Cell 415-555-0267
Service.LagoonSolutions@mailbeam.net

```html
<!DOCTYPE html>
<html lang="en">
<head>
<meta charset="utf-8">
<title>Lagoonworks Solutions – Business Card</title>
<link rel="stylesheet" href="https://fonts.googleapis.com/css2?family=Lato:wght@300;400;700&display=swap">
<style>
  :root {
    --page-bg: #e9ecef;
    --band-black: #0b0f12;
    --band-black-edge: #1c2328;
    --blue-deep: #1a8fd0;
    --blue-mid: #2aa6e0;
    --blue-light: #45c0ec;
    --logo-blue: #2fb6ea;
    --ink-dark: #0d2433;
    --ink-white: #ffffff;
    --icon-dark: #123247;
  }
  * { margin: 0; padding: 0; box-sizing: border-box; }
  html, body {
    width: 1200px;
    height: 1023px;
    overflow: hidden;
    background: var(--page-bg);
    font-family: "Lato", Arial, sans-serif;
  }
  .stage {
    width: 1200px;
    height: 1023px;
    display: flex;
    align-items: center;
    justify-content: center;
  }
  .card {
    position: relative;
    width: 900px;
    height: 514px;
    border-radius: 6px;
    overflow: hidden;
    background: linear-gradient(160deg, var(--blue-light) 0%, var(--blue-mid) 45%, var(--blue-deep) 100%);
    box-shadow: 0 18px 40px rgba(0, 0, 0, 0.25);
  }
  .header-band {
    position: absolute;
    left: 0; top: 0;
    width: 100%;
    height: 196px;
    background: linear-gradient(180deg, var(--band-black-edge) 0%, var(--band-black) 100%);
  }
  .brand {
    position: absolute;
    right: 70px;
    top: 40px;
    display: flex;
    align-items: center;
    gap: 26px;
  }
  .brand-dot {
    width: 44px;
    height: 44px;
    border-radius: 50%;
    background: var(--logo-blue);
  }
  .brand-name {
    color: var(--logo-blue);
    font-weight: 300;
    font-size: 46px;
    line-height: 1.1;
    letter-spacing: 3px;
    text-align: right;
  }
  .gear-decoration {
    position: absolute;
    right: 0;
    top: 196px;
    width: 300px;
    height: 318px;
    background: radial-gradient(circle at 70% 40%, rgba(26, 143, 208, 0.55) 0%, rgba(26, 143, 208, 0) 70%);
  }
  .contact {
    position: absolute;
    left: 70px;
    top: 228px;
  }
  .person-name {
    color: var(--ink-dark);
    font-size: 34px;
    font-weight: 400;
    letter-spacing: 2px;
    text-transform: uppercase;
  }
  .person-role {
    color: var(--ink-white);
    font-size: 22px;
    font-weight: 300;
    margin-top: 8px;
    margin-bottom: 34px;
  }
  .contact-list { list-style: none; }
  .contact-item {
    display: flex;
    align-items: center;
    gap: 14px;
    color: var(--ink-white);
    font-size: 24px;
    font-weight: 400;
    margin-bottom: 12px;
  }
  .contact-icon { width: 28px; height: 28px; flex: none; }
</style>
</head>
<body>
<main class="stage">
  <article class="card">
    <header class="header-band">
      <div class="brand">
        <span class="brand-dot"></span>
        <div class="brand-name">LAGOONWORKS<br>SOLUTIONS LLC</div>
      </div>
    </header>

    <div class="gear-decoration" role="img" aria-label="Faint interlocking gear decoration"></div>

    <section class="contact">
      <h1 class="person-name">Jonathan R. Delvoy</h1>
      <p class="person-role">Owner</p>
      <ul class="contact-list">
        <li class="contact-item">
          <svg class="contact-icon" viewBox="0 0 28 28" aria-hidden="true">
            <circle cx="14" cy="14" r="14" fill="var(--icon-dark)"/>
            <path d="M9 8c1-1 2-1 2.6 0l1.4 2.4c.4.7.2 1.3-.4 1.8l-.8.6c.7 1.6 1.9 2.8 3.4 3.5l.7-.8c.5-.6 1.2-.7 1.8-.3l2.3 1.4c.9.6.9 1.6 0 2.5-1.5 1.5-3.6 1.6-6.2-.4-2.3-1.8-4.3-4.3-4.9-6.6-.4-1.6 0-3 .1-4.1z" fill="#fff"/>
          </svg>
          415-555-0182
        </li>
        <li class="contact-item">
          <svg class="contact-icon" viewBox="0 0 28 28" aria-hidden="true">
            <circle cx="14" cy="14" r="14" fill="var(--icon-dark)"/>
            <rect x="9.5" y="6.5" width="9" height="15" rx="1.6" fill="#fff"/>
            <rect x="11" y="8.5" width="6" height="9" fill="var(--icon-dark)"/>
            <circle cx="14" cy="19.5" r="0.9" fill="var(--icon-dark)"/>
          </svg>
          415-555-0267
        </li>
        <li class="contact-item">
          <svg class="contact-icon" viewBox="0 0 28 28" aria-hidden="true">
            <circle cx="14" cy="14" r="14" fill="var(--icon-dark)"/>
            <rect x="7" y="9" width="14" height="10" rx="1" fill="#fff"/>
            <path d="M7.5 9.5 14 14.5l6.5-5" fill="none" stroke="var(--icon-dark)" stroke-width="1.4"/>
          </svg>
          Service.LagoonSolutions@mailbeam.net
        </li>
      </ul>
    </section>
  </article>
</main>
</body>
</html>
```